In Search of a FANTASTIC BUSINESS CARD REFRESH AND REDESIGN

I would like to redesign the current business card for my company.  There is a parent company, Brookfane Care Group, with 2 operating companies - Brookfane Homecare and Brookfane Senior Living.
I will include the current business card design, along with the 3 logos I would like incorporated.  The business card can be two sided.  I'm looking for something clean, professional, and a fresh new look.

Target Market(s)
Hospitals, social workers, insurance agents, family members of seniors
Industry/Entity Type
Healthcare
Contact Information for Business Card
Name, title of person, address, phone number, web address, email address
Look and feel
Each slider illustrates characteristics of the customer's brand and the style your logo design should communicate.

```html
<!DOCTYPE html>
<html lang="en">
<head>
<meta charset="utf-8">
<title>Brookfane Homecare – Business Card</title>
<link href="https://fonts.googleapis.com/css2?family=Libre+Baskerville&display=swap" rel="stylesheet">
<style>
  :root {
    --bg: #dcdde1;
    --card-dark: #6b6b6d;
    --card-dark-hi: #7f7f81;
    --card-light: #f7f7f7;
    --coral: #ec8f8b;
    --teal: #3f8584;
    --ink: #4d4d4f;
    --black: #111111;
    --white: #ffffff;
  }
  * { margin: 0; padding: 0; box-sizing: border-box; }
  html, body { width: 1200px; height: 800px; overflow: hidden; }
  body {
    background: var(--bg);
    font-family: "Libre Baskerville", Georgia, serif;
    position: relative;
  }
  .card {
    position: absolute;
    left: 390px;
    width: 420px;
    height: 240px;
    border-radius: 14px;
    overflow: hidden;
  }
  .card--front {
    top: 130px;
    background: linear-gradient(160deg, var(--card-dark) 20%, var(--card-dark-hi) 100%);
    display: flex;
    flex-direction: column;
    align-items: center;
    justify-content: center;
    gap: 16px;
  }
  .front-mark {
    width: 54px;
    height: 54px;
    border-radius: 8px;
    background: var(--coral);
  }
  .front-name {
    color: var(--white);
    font-size: 24px;
    letter-spacing: 0.5px;
  }
  .card--back {
    top: 430px;
    background: linear-gradient(150deg, #ececec 0%, var(--card-light) 45%, var(--white) 100%);
    color: var(--ink);
  }
  .person {
    position: absolute;
    left: 36px;
    top: 32px;
  }
  .person__name {
    font-size: 21px;
    letter-spacing: 0.4px;
    line-height: 1.2;
  }
  .person__title {
    font-size: 16px;
    color: var(--teal);
    margin-top: 4px;
  }
  .contact {
    position: absolute;
    left: 36px;
    font-size: 11px;
    line-height: 15px;
  }
  .contact--address { top: 106px; width: 150px; }
  .contact--lines { top: 150px; list-style: none; }
  .contact__row { display: flex; align-items: center; gap: 4px; }
  .icon { width: 9px; height: 9px; flex: none; }
  .icon path, .icon circle, .icon rect { fill: none; stroke: var(--teal); stroke-width: 1.3; }
  .icon .solid { fill: var(--teal); stroke: none; }
  .address-line { display: flex; gap: 4px; }
  .brands {
    position: absolute;
    right: 44px;
    bottom: 34px;
    display: flex;
    gap: 22px;
    align-items: flex-start;
  }
  .brand {
    display: flex;
    flex-direction: column;
    align-items: center;
    gap: 6px;
    width: 78px;
    text-align: center;
    font-size: 11px;
    line-height: 1.25;
  }
  .brand__mark { width: 24px; height: 24px; border-radius: 4px; }
  .brand--senior .brand__mark { background: var(--teal); }
  .brand--senior .brand__name { color: var(--teal); }
  .brand--group .brand__mark { background: var(--black); }
  .brand--group .brand__name { color: var(--black); }
</style>
</head>
<body>

<section class="card card--front" aria-label="Card front">
  <div class="front-mark"></div>
  <div class="front-name">Brookfane Homecare</div>
</section>

<section class="card card--back" aria-label="Card back">
  <div class="person">
    <h1 class="person__name">MARLA PENNICK</h1>
    <p class="person__title">President, CEO</p>
  </div>

  <div class="contact contact--address">
    <div class="address-line">
      <svg class="icon" viewBox="0 0 10 10"><path d="M5 9.3 C2.5 6.3 1.6 5 1.6 3.6 A3.4 3.4 0 0 1 8.4 3.6 C8.4 5 7.5 6.3 5 9.3Z"/><circle cx="5" cy="3.6" r="1.2"/></svg>
      <span>480 Larkspur Ave, Suite 210, Fairhaven, HI 96790</span>
    </div>
  </div>

  <ul class="contact contact--lines">
    <li class="contact__row">
      <svg class="icon" viewBox="0 0 10 10"><path d="M2 1 L3.8 1 L4.5 3.2 L3.4 4 C4 5.3 4.8 6.1 6 6.6 L6.8 5.5 L9 6.2 L9 8 C9 8.6 8.5 9 8 9 C4.3 8.7 1.3 5.7 1 2 C1 1.5 1.4 1 2 1Z"/></svg>
      <span>(555) 014-2286</span>
    </li>
    <li class="contact__row">
      <svg class="icon" viewBox="0 0 10 10"><rect class="solid" x="2.5" y="1" width="5" height="2.5"/><rect class="solid" x="1" y="4" width="8" height="3.5"/><rect class="solid" x="2.5" y="7.8" width="5" height="1.6"/></svg>
      <span>(555) 014-2290</span>
    </li>
    <li class="contact__row">
      <svg class="icon" viewBox="0 0 10 10"><rect x="1" y="2.5" width="8" height="5.5"/><path d="M1 2.5 L5 5.8 L9 2.5"/></svg>
      <span>Marla@brookfanecare.com</span>
    </li>
    <li class="contact__row">
      <svg class="icon" viewBox="0 0 10 10"><circle cx="5" cy="5" r="4"/><path d="M1 5 H9 M5 1 C3 3.5 3 6.5 5 9 C7 6.5 7 3.5 5 1"/></svg>
      <span>www.brookfanecare.com</span>
    </li>
  </ul>

  <div class="brands">
    <div class="brand brand--senior">
      <div class="brand__mark"></div>
      <div class="brand__name">Brookfane Senior Living</div>
    </div>
    <div class="brand brand--group">
      <div class="brand__mark"></div>
      <div class="brand__name">Brookfane Care Group</div>
    </div>
  </div>
</section>

</body>
</html>
```